Need high-end luxury business cards with raised element of logo

Looking for a non-standard business card with the option of part of our logo elements to be printed as raised or embossed. Would like at least 5 different photos on the backside. Looking at printing through this: https://www.cardvellox.com/raised-spot-uv-business-cards.html

updated the logo file

```html
<!DOCTYPE html>
<html lang="en">
<head>
<meta charset="utf-8">
<title>Larchmont Row — Business Card</title>
<link rel="stylesheet" href="https://fonts.googleapis.com/css2?family=Roboto:wght@300;400;700&display=swap">
<style>
  :root {
    --canvas: #e4e5e7;
    --card: #34546b;
    --ink: #ffffff;
    --ink-soft: #d7e1e8;
    --rule: rgba(255,255,255,0.55);
  }
  * { box-sizing: border-box; margin: 0; padding: 0; }
  html, body { width: 1200px; height: 800px; overflow: hidden; }
  body {
    background: var(--canvas);
    font-family: "Roboto", Arial, sans-serif;
    color: var(--ink);
    position: relative;
  }
  .card {
    position: absolute;
    width: 560px;
    height: 320px;
    left: 320px;
    background: var(--card);
    box-shadow: 0 6px 18px rgba(0,0,0,0.18);
    overflow: hidden;
  }
  .card--front { top: 52px; }
  .card--back { top: 428px; }

  /* front */
  .brand {
    position: absolute;
    top: 80px;
    right: 40px;
    width: 260px;
    text-align: center;
  }
  .brand__name {
    font-size: 26px;
    font-weight: 400;
    letter-spacing: 3px;
    text-transform: uppercase;
    white-space: nowrap;
    color: var(--ink);
  }
  .brand__rule {
    height: 1px;
    background: var(--rule);
    margin: 12px auto 0;
    width: 180px;
  }
  .divider {
    position: absolute;
    left: 250px;
    right: 28px;
    top: 150px;
    height: 1px;
    background: var(--rule);
  }
  .address {
    position: absolute;
    right: 30px;
    top: 164px;
    text-align: right;
    font-size: 14px;
    line-height: 1.45;
    font-weight: 300;
    font-style: normal;
  }
  .address__web { font-weight: 400; }
  .address__web b { font-weight: 700; }
  .person {
    position: absolute;
    left: 32px;
    top: 162px;
  }
  .person__name {
    font-size: 21px;
    font-weight: 700;
    letter-spacing: 0.5px;
    text-transform: uppercase;
  }
  .person__title {
    font-size: 14px;
    font-weight: 300;
    color: var(--ink-soft);
    margin-top: 2px;
  }
  .person__rule {
    width: 150px;
    height: 1px;
    background: var(--rule);
    margin: 8px 0 6px;
  }
  .contacts { list-style: none; }
  .contacts li {
    display: flex;
    align-items: center;
    gap: 9px;
    font-size: 14px;
    line-height: 1.4;
    font-weight: 300;
  }
  .contacts svg { width: 12px; height: 12px; fill: var(--ink); flex: none; }

  /* back */
  .gallery {
    position: absolute;
    inset: 14px;
    display: grid;
    grid-template-columns: 2fr 3fr 5fr;
    grid-template-rows: 1fr 1fr;
    grid-template-areas:
      "porch balcony valley"
      "lounge lounge spa";
    gap: 8px;
  }
  .photo { width: 100%; height: 100%; }
  .photo--porch { grid-area: porch; background: linear-gradient(170deg, #b8763a 0%, #5a3520 60%, #8a6a52 100%); }
  .photo--balcony { grid-area: balcony; background: linear-gradient(160deg, #d98a3a 0%, #6b3d22 55%, #c9b7a4 100%); }
  .photo--valley { grid-area: valley; background: linear-gradient(200deg, #9aa7b1 0%, #c78a2e 35%, #8d6a25 70%, #5f6a2e 100%); }
  .photo--lounge { grid-area: lounge; background: linear-gradient(180deg, #7a3f1c 0%, #c9702c 45%, #5a2c14 100%); }
  .photo--spa { grid-area: spa; background: linear-gradient(170deg, #5e5b7c 0%, #3a3032 45%, #2fb7b4 80%, #4a3b33 100%); }
  .seal {
    position: absolute;
    left: 50%;
    top: 50%;
    width: 118px;
    height: 118px;
    transform: translate(-50%, -50%);
    border-radius: 50%;
    background: var(--card);
    display: flex;
    align-items: center;
    justify-content: center;
    text-align: center;
  }
  .seal__name {
    font-size: 13px;
    font-weight: 400;
    letter-spacing: 1.5px;
    text-transform: uppercase;
    line-height: 1.3;
    color: var(--ink);
  }
</style>
</head>
<body>
  <section class="card card--front" aria-label="Business card front">
    <div class="brand">
      <div class="brand__name">Larchmont Row</div>
      <div class="brand__rule"></div>
    </div>
    <div class="divider"></div>
    <address class="address">
      Larchmont Row<br>
      4120 Juniper Court<br>
      Boulder Ridge, Montana 59801<br>
      <span class="address__web">www.<b>larchmontrow</b>.com</span>
    </address>
    <div class="person">
      <div class="person__name">Daniel Hayes</div>
      <div class="person__title">President</div>
      <div class="person__rule"></div>
      <ul class="contacts">
        <li><svg viewBox="0 0 24 24"><path d="M6.6 10.8a15.1 15.1 0 0 0 6.6 6.6l2.2-2.2a1 1 0 0 1 1-.25 11.4 11.4 0 0 0 3.6.57 1 1 0 0 1 1 1V20a1 1 0 0 1-1 1A17 17 0 0 1 3 4a1 1 0 0 1 1-1h3.5a1 1 0 0 1 1 1c0 1.25.2 2.45.57 3.57a1 1 0 0 1-.25 1z"/></svg>555-210-4871</li>
        <li><svg viewBox="0 0 24 24"><path d="M7 1h10a2 2 0 0 1 2 2v18a2 2 0 0 1-2 2H7a2 2 0 0 1-2-2V3a2 2 0 0 1 2-2zm0 3v14h10V4z"/></svg>555-318-2094</li>
        <li><svg viewBox="0 0 24 24"><path d="M9 3h6a2 2 0 0 1 2 2v2h4a1 1 0 0 1 1 1v11a2 2 0 0 1-2 2H4a2 2 0 0 1-2-2V8a1 1 0 0 1 1-1h4V5a2 2 0 0 1 2-2zm0 4h6V5H9z"/></svg>555-426-7310</li>
        <li><svg viewBox="0 0 24 24"><path d="M2 5h20v14H2zm2 2v.5l8 5 8-5V7z"/></svg>hello@larchmontrow.com</li>
      </ul>
    </div>
  </section>

  <section class="card card--back" aria-label="Business card back">
    <div class="gallery">
      <div class="photo photo--porch" role="img" aria-label="Photo: wooden porch corner with autumn trees beyond the railing"></div>
      <div class="photo photo--balcony" role="img" aria-label="Photo: covered balcony with sofa overlooking an autumn valley at sunset"></div>
      <div class="photo photo--valley" role="img" aria-label="Photo: aerial view of a lodge on a mountainside of autumn forest"></div>
      <div class="photo photo--lounge" role="img" aria-label="Photo: log cabin living room with a lit stone fireplace"></div>
      <div class="photo photo--spa" role="img" aria-label="Photo: glowing hot tub on a covered deck at dusk with mountain view"></div>
    </div>
    <div class="seal"><div class="seal__name">Larchmont<br>Row</div></div>
  </section>
</body>
</html>
```